Laundry Store front design

I own a laundry business and require a design for the shop front.

I have uploaded 3 photos with window numbers on, 1 thru 5. It might be better to stich these together as I want the design to flow across 1-5 but only the top of 3.

I have uploaded some pdf documents with more details.

Font styles to use
Serif

Colors
0054AA
0677BA
7BADD7
CADEEF
E8F1F8

```html
<!DOCTYPE html>
<html lang="en">
<head>
<meta charset="utf-8">
<title>Crestline Laundry Services – Shop Front Windows</title>
<link rel="stylesheet" href="https://fonts.googleapis.com/css2?family=Exo+2:ital,wght@1,800;1,900&family=Montserrat:ital,wght@0,500;0,700;0,800;1,700;1,800&display=swap">
<style>
:root{
  --navy:#0b1730;
  --deep:#0054AA;
  --mid:#0677BA;
  --sky:#1596d3;
  --soft:#7BADD7;
  --pale:#CADEEF;
  --mist:#E8F1F8;
  --white:#ffffff;
  --red:#e0262c;
  --green:#2f9e44;
  --gap:#3b3a36;
  --page:#eef1f4;
}
*{margin:0;padding:0;box-sizing:border-box}
html,body{width:1200px;height:2700px;overflow:hidden;background:var(--page)}
body{font-family:"Montserrat",Arial,sans-serif;color:var(--white)}
.section{position:relative;width:1200px;height:900px}
.pane{position:absolute;overflow:hidden;background:var(--navy);border:4px solid var(--gap)}
.pane.transom{background:linear-gradient(160deg,var(--deep),var(--sky))}
.pane.transom.light{background:linear-gradient(160deg,var(--mid),#1fb0e8)}
.wave{position:absolute;left:0;bottom:0;width:100%;height:38%}
.photo{position:absolute;border-radius:50%;border:6px solid var(--white)}
.photo.plain{border:none}
.headline{position:absolute;font-family:"Exo 2",Arial,sans-serif;font-style:italic;font-weight:900;font-size:36px;letter-spacing:1px;color:var(--white);text-shadow:0 2px 4px rgba(0,0,0,.35)}
.bubble{position:absolute;border-radius:50%;background:var(--sky);box-shadow:inset -2px -2px 0 rgba(255,255,255,.5)}
.bubble.dark{background:#5b6677}
.bullets{position:absolute;list-style:none;font-weight:800;font-style:italic;text-transform:uppercase}
.bullets li{position:relative;padding-left:14px}
.bullets li::before{content:"";position:absolute;left:0;top:.45em;width:7px;height:7px;border-radius:50%;background:var(--sky)}
.bullets.light li::before{background:var(--pale)}
.bullets.dark{color:var(--deep)}
.button{position:absolute;background:var(--mid);color:var(--white);font-weight:800;text-align:center;border-radius:3px}
.tag{position:absolute;background:var(--red);color:var(--white);font-weight:800;font-size:14px;padding:6px 12px 6px 22px;clip-path:polygon(12px 0,100% 0,100% 100%,12px 100%,0 50%);white-space:nowrap}
.caption{position:absolute;background:var(--mid);color:var(--white);font-weight:700;font-size:10px;text-align:center;padding:4px 0}
.list-circle{position:absolute;border-radius:50%;background:radial-gradient(circle at 40% 35%,var(--sky),var(--deep));border:5px solid var(--white)}
.hours{position:absolute;font-size:10.5px;font-weight:800;font-style:italic;border-spacing:0;line-height:15px}
.hours .day{width:86px;padding-right:6px}
.hours .time{width:74px;white-space:nowrap}
</style>
</head>
<body>
<svg width="0" height="0" style="position:absolute">
  <defs>
    <linearGradient id="waveFill" x1="0" y1="0" x2="0" y2="1">
      <stop offset="0" stop-color="#ffffff"/>
      <stop offset="1" stop-color="#CADEEF"/>
    </linearGradient>
    <symbol id="wave" viewBox="0 0 100 100" preserveAspectRatio="none">
      <path d="M0 22 Q45 0 100 6 L100 100 L0 100Z" fill="#0677BA"/>
      <path d="M0 32 Q45 10 100 16 L100 100 L0 100Z" fill="url(#waveFill)"/>
    </symbol>
  </defs>
</svg>

<!-- Front one: special pricing, contact, discount -->
<section class="section front-one">
  <div class="pane transom" style="left:40px;top:100px;width:204px;height:140px"></div>
  <div class="pane transom" style="left:248px;top:100px;width:196px;height:140px"></div>
  <div class="pane transom" style="left:448px;top:100px;width:136px;height:140px">
    <div class="photo" role="img" aria-label="Hands holding a freshly laundered shirt" style="left:8px;top:8px;width:116px;height:116px;background:linear-gradient(135deg,#c9a08a,#e9eef5)"></div>
  </div>
  <div class="headline" style="left:70px;top:148px">SPECIAL</div>
  <div class="headline" style="left:272px;top:148px">PRICING</div>

  <div class="pane" style="left:40px;top:256px;width:204px;height:544px"><svg class="wave"><use href="#wave"/></svg></div>
  <div class="pane" style="left:248px;top:256px;width:196px;height:544px"><svg class="wave"><use href="#wave"/></svg></div>
  <div class="pane" style="left:448px;top:256px;width:136px;height:544px"><svg class="wave"><use href="#wave"/></svg></div>
  <div class="photo" role="img" aria-label="Row of commercial washing machines in a laundromat" style="left:48px;top:330px;width:240px;height:240px;background:linear-gradient(150deg,#f4f6f8,#7c8797)"></div>
  <div class="photo" role="img" aria-label="Man ironing a garment" style="left:140px;top:540px;width:130px;height:130px;background:linear-gradient(150deg,#43b3d8,#d6dde4)"></div>
  <div class="list-circle" style="left:250px;top:430px;width:180px;height:180px"></div>
  <ul class="bullets light" style="left:284px;top:470px;font-size:11px;line-height:16px">
    <li>Property<br>managers</li><li>Hotels</li><li>Apartments</li><li>Villas</li><li>Restaurants</li><li>More.</li>
  </ul>
  <div class="bubble" style="left:330px;top:395px;width:16px;height:16px"></div>
  <div class="bubble" style="left:352px;top:380px;width:10px;height:10px"></div>
  <div class="bubble dark" style="left:360px;top:360px;width:8px;height:8px"></div>
  <div class="bubble" style="left:530px;top:350px;width:14px;height:14px"></div>
  <div class="bubble dark" style="left:548px;top:330px;width:7px;height:7px"></div>

  <div class="pane transom" style="left:620px;top:100px;width:144px;height:140px"></div>
  <div class="pane transom" style="left:768px;top:100px;width:196px;height:140px"></div>
  <div class="pane transom light" style="left:968px;top:100px;width:192px;height:140px"></div>
  <svg style="position:absolute;left:640px;top:150px" width="34" height="34" viewBox="0 0 34 34" aria-hidden="true">
    <circle cx="17" cy="17" r="16" fill="#0b1730"/>
    <path d="M11 9c1-1 2.5-1 3 0l2 3c.4.8 0 1.6-.6 2l-1.3 1c.9 2 2.5 3.6 4.5 4.5l1-1.3c.5-.6 1.3-1 2-.6l3 2c1 .6 1 2 0 3-1.7 1.7-4.5 2-7 .3-3.6-2.3-6.3-5-8.4-8.6C7.6 12.9 9 10.6 11 9z" fill="#fff"/>
  </svg>
  <div class="headline" style="left:684px;top:152px;font-size:28px">+357&nbsp;&nbsp;&nbsp;24555180</div>
  <div class="tag" style="left:984px;top:160px">CONTACT NOW</div>

  <div class="pane" style="left:620px;top:256px;width:144px;height:544px"><svg class="wave"><use href="#wave"/></svg></div>
  <div class="pane" style="left:768px;top:256px;width:196px;height:544px"><svg class="wave"><use href="#wave"/></svg></div>
  <div class="pane" style="left:968px;top:256px;width:192px;height:544px"><svg class="wave"><use href="#wave"/></svg></div>
  <div role="img" aria-label="Laundry attendant in uniform holding folded towels" style="position:absolute;left:628px;top:264px;width:128px;height:380px;background:linear-gradient(180deg,#dfe7ee,#7BADD7 70%,#CADEEF)"></div>
  <div class="caption" style="left:634px;top:742px;width:116px">WITHIN LOCAL AREA</div>

  <div style="position:absolute;left:800px;top:300px;background:var(--mid);padding:4px 12px;border-radius:4px;font-family:'Exo 2',sans-serif;font-style:italic;font-weight:900;font-size:42px;line-height:44px">20<span style="font-size:24px">%</span><span style="font-size:11px"> OFF</span></div>
  <div style="position:absolute;left:818px;top:354px;background:var(--red);padding:3px 10px;font-weight:800;font-size:15px">DISCOUNT</div>
  <div style="position:absolute;left:808px;top:382px;font-weight:700;font-size:14px">FIRST ORDER</div>
  <svg style="position:absolute;left:806px;top:418px" width="26" height="34" viewBox="0 0 26 34" aria-hidden="true">
    <path d="M13 1C6.4 1 1 6.2 1 12.6 1 21 13 33 13 33s12-12 12-20.4C25 6.2 19.6 1 13 1z" fill="#1596d3"/>
    <circle cx="13" cy="12.5" r="4.5" fill="#0b1730"/>
  </svg>
  <div style="position:absolute;left:840px;top:420px;font-weight:800;font-style:italic;font-size:16px;line-height:17px">FREE<br>DELIVERY</div>
  <div class="caption" style="left:782px;top:742px;width:168px;font-size:9px">WWW.CRESTLINELAUNDRY.COM.CY</div>

  <div class="bubble" style="left:990px;top:330px;width:16px;height:16px"></div>
  <div class="bubble dark" style="left:1010px;top:312px;width:8px;height:8px"></div>
  <div class="bubble" style="left:980px;top:360px;width:10px;height:10px"></div>
  <div class="photo" role="img" aria-label="Folded shirt delivered in a cardboard box" style="left:1000px;top:370px;width:150px;height:150px;border-color:var(--mid);background:linear-gradient(135deg,#eef2f7,#8d97a6)"></div>
  <div class="button" style="left:990px;top:740px;width:150px;padding:7px 0;font-size:15px">BOOK ONLINE</div>
</section>

<!-- Front two: welcome, brand, opening hours -->
<section class="section front-two">
  <div class="pane transom" style="left:140px;top:100px;width:304px;height:140px">
    <div class="photo" role="img" aria-label="Smiling woman holding clean clothes on hangers" style="left:60px;top:6px;width:180px;height:180px;background:linear-gradient(135deg,#f3e6df,#c46a8a)"></div>
  </div>
  <div class="pane transom light" style="left:448px;top:100px;width:316px;height:140px"></div>
  <div class="pane transom light" style="left:768px;top:100px;width:292px;height:140px"></div>
  <div class="headline" style="left:808px;top:150px;font-size:40px">RESIDENTS</div>

  <div class="pane" style="left:140px;top:256px;width:304px;height:544px">
    <div style="position:absolute;left:0;bottom:0;width:100%;height:45%;background:linear-gradient(180deg,#fff,var(--mist))"></div>
  </div>
  <div class="pane" style="left:448px;top:256px;width:316px;height:544px"><svg class="wave"><use href="#wave"/></svg></div>
  <div class="pane" style="left:768px;top:256px;width:292px;height:544px"><svg class="wave"><use href="#wave"/></svg></div>

  <div style="position:absolute;left:206px;top:330px;width:150px;text-align:center">
    <div style="background:var(--mid);border-radius:8px 8px 0 0;padding:4px 0;font-weight:800;line-height:1"><span style="font-size:13px">WE'RE</span><br><span style="font-size:34px">OPEN</span></div>
    <div style="background:var(--green);margin-left:20px;padding:5px 0;font-weight:800;font-size:16px">COME IN</div>
  </div>

  <div style="position:absolute;left:470px;top:400px;width:272px;text-align:center">
    <div style="font-weight:800;font-size:48px;color:var(--sky);line-height:1">crestline</div>
    <div style="font-weight:500;font-size:20px;letter-spacing:4px;margin-top:4px">Laundry Services</div>
  </div>
  <ul class="bullets dark" style="left:520px;top:690px;font-size:12px;line-height:17px">
    <li>Service washes</li><li>Ironing service</li><li>Duvets</li><li>Linen</li><li>Towels</li>
  </ul>

  <div class="bubble" style="left:800px;top:290px;width:16px;height:16px"></div>
  <div class="bubble dark" style="left:820px;top:276px;width:8px;height:8px"></div>
  <div class="bubble" style="left:782px;top:318px;width:10px;height:10px"></div>
  <div class="list-circle" style="left:800px;top:330px;width:240px;height:240px;background:radial-gradient(circle at 40% 35%,var(--mid),var(--deep))"></div>
  <div style="position:absolute;left:860px;top:360px;font-family:'Exo 2',sans-serif;font-style:italic;font-weight:900;font-size:20px;line-height:18px">HOURS<span style="font-size:11px"> OF</span><br><span style="font-family:'Montserrat',sans-serif;font-style:normal;font-weight:500">OPENING</span></div>
  <table class="hours" style="left:840px;top:404px">
    <tr><td class="day">MONDAY</td><td class="time">9:00 - 5:00</td></tr>
    <tr><td class="day">TUESDAY</td><td class="time">9:00 - 5:00</td></tr>
    <tr><td class="day">WEDNESDAY</td><td class="time">9:00 - 5:00</td></tr>
    <tr><td class="day">THURSDAY</td><td class="time">9:00 - 5:00</td></tr>
    <tr><td class="day">FRIDAY</td><td class="time">9:00 - 5:00</td></tr>
    <tr><td class="day">SATURDAY</td><td class="time">9:00 - 12:00</td></tr>
    <tr><td class="day">SUNDAY</td><td class="time" style="text-align:center">CLOSED</td></tr>
  </table>
  <ul class="bullets dark" style="left:820px;top:690px;font-size:12px;line-height:17px">
    <li>Wedding dresses</li><li>Upholstery</li><li>Rugs</li><li>Collection</li><li>Delivery</li>
  </ul>
</section>

<!-- Front three: wet cleaning, wash dry fold -->
<section class="section front-three">
  <div class="pane transom" style="left:40px;top:100px;width:164px;height:140px">
    <div class="photo plain" role="img" aria-label="Hand loading clothes into a front-loading washer" style="left:8px;top:6px;width:128px;height:128px;background:linear-gradient(135deg,#e2e6ea,#6d7784)"></div>
  </div>
  <div class="pane transom" style="left:208px;top:100px;width:96px;height:140px"></div>
  <div class="pane transom" style="left:308px;top:100px;width:96px;height:140px"></div>
  <div class="pane transom light" style="left:408px;top:100px;width:192px;height:140px"></div>

  <div class="pane" style="left:40px;top:256px;width:164px;height:544px">
    <div style="position:absolute;left:0;bottom:0;width:100%;height:24%;background:linear-gradient(180deg,#fff,var(--mist))"></div>
  </div>
  <div class="pane" style="left:208px;top:256px;width:196px;height:544px"><svg class="wave"><use href="#wave"/></svg></div>
  <div class="pane" style="left:408px;top:256px;width:192px;height:544px"><svg class="wave"><use href="#wave"/></svg></div>

  <div style="position:absolute;left:54px;top:400px;width:136px;text-align:center">
    <div style="font-weight:800;font-size:22px;color:var(--sky)">GentleRinse</div>
    <div style="font-weight:500;font-size:11px;letter-spacing:2px;color:var(--sky)">WET CLEANING</div>
  </div>

  <div class="bubble" style="left:236px;top:296px;width:14px;height:14px"></div>
  <div class="bubble dark" style="left:222px;top:290px;width:7px;height:7px"></div>
  <ul class="bullets" style="left:222px;top:350px;width:170px;font-size:10px;line-height:14px">
    <li>Specially adapted machines</li><li>Eco-friendly, no harsh chemicals</li><li>VIP 2 hour service available</li><li>Superior stain removal</li><li>Suitable for all 'dry clean only' garments</li>
  </ul>
  <div class="photo" role="img" aria-label="Two women holding stacks of folded laundry" style="left:428px;top:330px;width:170px;height:170px;border-color:var(--mid);background:linear-gradient(135deg,#f1ece6,#9aa6b4)"></div>
  <div class="bubble" style="left:460px;top:296px;width:12px;height:12px"></div>
  <div role="img" aria-label="Pile of neatly folded colourful clothes" style="position:absolute;left:300px;top:560px;width:190px;height:120px;border-radius:8px;background:linear-gradient(135deg,#e2323a,#5a8ec7)"></div>

  <div class="pane transom" style="left:640px;top:100px;width:144px;height:140px"></div>
  <div class="pane transom light" style="left:788px;top:100px;width:176px;height:140px"></div>
  <div class="pane transom light" style="left:968px;top:100px;width:192px;height:140px"></div>
  <div class="headline" style="left:1000px;top:150px;font-size:34px">SERVICE</div>

  <div class="pane" style="left:640px;top:256px;width:144px;height:544px"><svg class="wave"><use href="#wave"/></svg></div>
  <div class="pane" style="left:788px;top:256px;width:176px;height:544px"><svg class="wave"><use href="#wave"/></svg></div>
  <div class="pane" style="left:968px;top:256px;width:192px;height:544px"><svg class="wave"><use href="#wave"/></svg></div>

  <div role="img" aria-label="Close-up of a washing machine door" style="position:absolute;left:644px;top:300px;width:136px;height:170px;border-radius:10px;background:linear-gradient(160deg,var(--sky),#0a3a66 55%,var(--navy))"></div>

  <ul class="bullets" style="left:806px;top:320px;font-size:17px;line-height:24px">
    <li>WASH</li><li>DRY</li><li>FOLD</li>
  </ul>
  <div style="position:absolute;left:806px;top:420px;font-weight:800;font-style:italic;font-size:14px">STARTING AT</div>
  <div style="position:absolute;left:806px;top:442px;background:var(--mid);padding:2px 8px;display:flex;align-items:center;gap:6px;font-weight:800;font-style:italic">
    <span style="font-size:32px;line-height:36px">2</span><span style="font-size:11px;line-height:12px">EUROS<br>PER KG</span>
  </div>

  <div role="img" aria-label="Woman holding a shirt on a hanger beside a smiling woman" style="position:absolute;left:976px;top:300px;width:176px;height:260px;border-radius:8px;background:linear-gradient(160deg,#e4394a,#2f5f4a 70%,#0b1730)"></div>
  <div class="photo" role="img" aria-label="Rack of garments on hangers" style="left:960px;top:620px;width:110px;height:110px;background:linear-gradient(135deg,#e9c2c8,#8e5a6a)"></div>
</section>
</body>
</html>
```